Weight loss surgery restaurant card

We need to create a card for patients who have undergone weight loss surgery to take to restaurants so they can request smaller meals. These patients have had surgery on their stomach so that they can only consume half to one cup of food at a time. So normal sized restaurant meals are way too big (and cost a lot). This card they can present to the restaurant to communicate the fact that they have had weight loss surgery and therefore request a smaller meal portion at reduced cost

Target Market(s)

Restaurants serving weight loss surgery patients

Industry/Entity Type

Health Care

Contact Information for Business Card

This will be a plastic card similar to business card size.

Requirements
Must have
• The front of the card should include the following text:
• The individual bearing this card has undergone weight loss surgery.
• This surgery restricts portion sizes to between half and one cup of food at a time.
• Please give consideration to allowing smaller portions of your regular meals to be ordered to reduce wastage and excess costs.
• Example: a half size portion priced at two thirds of usual cost.
• The back of the card will have spaces for the person to write certain information. These are the categories that can be filled in by hand:
• Name:
• Procedure performed:
• Date of procedure (month/year):
• Treating Clinic Name:
• Treating Clinic Signature:
• Somewhere down the bottom should be something along the lines of:
• supplied from marcuswheelan.com.au
Nice to have
• A nice design with imagery/colours etc ... not just the text on a white background! Bright attractive colours preferred.
• I have uploaded my logo ... a roughly triangular image followed by my name etc. The triangular logo image could be used somewhere on the card and this logo can be interchangeable for other clinics who purchase the card.
• **Please note that I don't want my name to be included as part of the logo on the card ... just use the triangular image on the side of the logo without the following name**
• Also, the colouring of the card does not have to reflect my logo colours as I am anticipating interchanging this logo with other logos if other clinics choose to adopt the card. I am interested to see other, more generic, colour choices as well as my logo colours

```html
<!DOCTYPE html>
<html lang="en">
<head>
<meta charset="utf-8">
<title>Restaurant Portion Card</title>
<link href="https://fonts.googleapis.com/css2?family=Open+Sans:wght@400;600&family=Noto+Serif:wght@400&display=swap" rel="stylesheet">
<style>
  :root {
    --page: #e6e6e6;
    --card: #fbfbfb;
    --teal: #0f9186;
    --teal-soft: #bfe3de;
    --ink: #1a1a1a;
    --rule: #222222;
    --white: #ffffff;
  }
  * { margin: 0; padding: 0; box-sizing: border-box; }
  html, body {
    width: 1200px; height: 864px; overflow: hidden;
    background: var(--page);
    font-family: "Open Sans", Arial, sans-serif;
    color: var(--ink);
  }
  .canvas { position: relative; width: 1200px; height: 864px; }
  .card {
    position: absolute;
    width: 560px; height: 353px;
    background: var(--card);
    box-shadow: 0 6px 18px rgba(0,0,0,0.18);
    overflow: hidden;
  }

  /* Information side */
  .card--info { left: 560px; top: 50px; }
  .info-backdrop {
    position: absolute; left: 210px; top: 30px;
    width: 290px; height: 290px; border-radius: 50%;
    background: var(--teal-soft); opacity: 0.55;
  }
  .info-list {
    position: absolute; left: 44px; top: 92px; right: 34px;
    list-style: none; font-size: 15px; line-height: 1.35;
  }
  .info-list li { position: relative; padding-left: 24px; margin-bottom: 2px; }
  .info-list li::before {
    content: ""; position: absolute; left: 2px; top: 5px;
    width: 11px; height: 11px; border-radius: 50%; background: var(--teal);
  }
  .info-list .example { padding-left: 24px; }
  .info-list .example::before { display: none; }

  /* Form side */
  .card--form { left: 80px; top: 440px; }
  .brand {
    position: absolute; left: 250px; top: 40px;
    display: flex; align-items: center; gap: 10px;
  }
  .brand-dot { width: 22px; height: 22px; border-radius: 50%; background: var(--teal); }
  .brand-name { font-size: 24px; font-weight: 600; color: var(--teal); letter-spacing: 0.5px; }

  .form-fields { position: absolute; left: 30px; top: 98px; right: 30px; }
  .field { display: flex; align-items: flex-end; height: 29px; font-size: 16px; }
  .field-label { white-space: nowrap; padding-right: 8px; }
  .field-line { flex: 1; border-bottom: 1.5px solid var(--rule); margin-bottom: 5px; }

  .footer-band {
    position: absolute; left: 0; bottom: 0; width: 100%; height: 96px;
    background: var(--teal);
    display: flex; align-items: center; justify-content: center;
  }
  .footer-text {
    font-family: "Noto Serif", Georgia, serif;
    font-size: 27px; color: var(--white); letter-spacing: 0.3px;
  }
</style>
</head>
<body>
<main class="canvas">
  <section class="card card--info" aria-label="Restaurant information side">
    <div class="info-backdrop" aria-hidden="true"></div>
    <ul class="info-list">
      <li>The individual bearing this card has undergone weight loss surgery</li>
      <li>This surgery restricts portion sizes to between half and one cup of food at a time</li>
      <li>Please give consideration to allowing smaller portions of your regular meals to be ordered to reduce wastage and excess costs.</li>
      <li class="example">Example: a half size portion priced at two thirds of usual cost.</li>
    </ul>
  </section>

  <section class="card card--form" aria-label="Patient details side">
    <div class="brand">
      <span class="brand-dot" aria-hidden="true"></span>
      <span class="brand-name">Marcus Wheelan</span>
    </div>
    <div class="form-fields">
      <div class="field"><span class="field-label">Name :</span><span class="field-line"></span></div>
      <div class="field"><span class="field-label">Procedure performed :</span><span class="field-line"></span></div>
      <div class="field"><span class="field-label">Date of procedure (month/year) :</span><span class="field-line"></span></div>
      <div class="field"><span class="field-label">Treating Clinic Name :</span><span class="field-line"></span></div>
      <div class="field"><span class="field-label">Treating Clinic Signature :</span><span class="field-line"></span></div>
    </div>
    <div class="footer-band">
      <p class="footer-text">supplied from marcuswheelan.com.au</p>
    </div>
  </section>
</main>
</body>
</html>
```